Book Cover for: TITLE Mend the Quiet Hours SUBTITLE For couples who don't want to break up

We need a full cover design for a book on relationships written by husband and wife team, Marla and Walter Dunmore, PhD. This book will offer hope for couples that are on the verge of breaking up but want to work things out and stay together. The theme is to teach couples about their own reactions to their partner, how moods affect a relationship, how to get creative to solving problems and how to have a good feeling towards your partner regardless of differences. This book is about hope. It is a positive look at relationships that feel hopeless.

Target Market(s)

Married or couples that are going through a difficult time and are considering splitting up due to, communication difficulties, addiction, affair. We imagine the book will appeal to women more than men but still want a cover that men would be comfortable picking up.

Colors

Designer to choose colors to be used in the design.

Requirements
Must have
• We want the cover to beautiful, intriguing, simple and uncomplicated. We don't want it overly busy, technical, or complex.
Nice to have
• MAYBE?? a broken heart being put back together.
Should not have
• No photo, no cartoon, no flowers, no couple (unless obscure and not gender specific).

```html
<!DOCTYPE html>
<html lang="en">
<head>
<meta charset="utf-8">
<title>Mend the Quiet Hours — Book Cover</title>
<link rel="stylesheet" href="https://fonts.googleapis.com/css2?family=Barlow+Condensed:wght@600;700&family=Montserrat:wght@600;700&display=swap">
<style>
  :root {
    --page-bg: #e4e4e4;
    --cover-bg: #000000;
    --ink-white: #ffffff;
    --ink-red: #d10000;
    --rule-red: #5a0000;
    --heart-light: #e42222;
    --heart-mid: #b50f12;
    --heart-dark: #6e0508;
  }
  * { margin: 0; padding: 0; box-sizing: border-box; }
  html, body {
    width: 1200px;
    height: 1200px;
    overflow: hidden;
    background: var(--page-bg);
  }
  .book-cover {
    position: absolute;
    left: 260px;
    top: 73px;
    width: 680px;
    height: 1054px;
    background: var(--cover-bg);
    color: var(--ink-white);
    text-align: center;
  }
  .title-line {
    position: absolute;
    left: 0;
    width: 100%;
    font-family: "Barlow Condensed", "Arial Narrow", sans-serif;
    font-weight: 700;
    text-transform: uppercase;
    line-height: 1;
  }
  .title-top {
    top: 20px;
    font-size: 200px;
    letter-spacing: 4px;
  }
  .title-middle {
    top: 186px;
    display: flex;
    align-items: center;
    justify-content: center;
    gap: 16px;
    font-size: 90px;
    font-weight: 600;
    padding: 0 49px;
  }
  .title-middle .rule {
    flex: 1;
    height: 2px;
    background: var(--ink-white);
  }
  .title-bottom {
    top: 256px;
    font-size: 262px;
    color: var(--ink-red);
    letter-spacing: 2px;
  }
  .divider {
    position: absolute;
    left: 30px;
    width: 620px;
    height: 1px;
    background: linear-gradient(90deg, transparent, var(--rule-red), var(--ink-red), var(--rule-red), transparent);
  }
  .divider-upper { top: 512px; }
  .divider-lower { top: 610px; }
  .subtitle {
    position: absolute;
    top: 525px;
    left: 0;
    width: 100%;
    font-family: "Montserrat", Arial, sans-serif;
    font-weight: 600;
    font-size: 34px;
    line-height: 40px;
    text-transform: uppercase;
    letter-spacing: 0.5px;
  }
  .heart-art {
    position: absolute;
    left: 157px;
    top: 638px;
    width: 369px;
    height: 354px;
  }
  .author-rule {
    position: absolute;
    top: 994px;
    left: 60px;
    width: 560px;
    height: 1px;
    background: #1a1a1a;
  }
  .authors {
    position: absolute;
    top: 1002px;
    left: 0;
    width: 100%;
    font-family: "Montserrat", Arial, sans-serif;
    font-weight: 700;
    font-size: 27px;
    line-height: 32px;
    text-transform: uppercase;
    letter-spacing: 0.5px;
  }
  .authors .amp { color: var(--ink-red); }
</style>
</head>
<body>
  <main class="book-cover">
    <h1>
      <span class="title-line title-top">Mend</span>
      <span class="title-line title-middle"><span class="rule"></span>The Quiet<span class="rule"></span></span>
      <span class="title-line title-bottom">Hours</span>
    </h1>

    <div class="divider divider-upper"></div>
    <p class="subtitle">For couples who<br>don't want to break up</p>
    <div class="divider divider-lower"></div>

    <svg class="heart-art" viewBox="0 0 369 354" role="img" aria-label="Illustration of a red fabric heart stitched back together with white thread">
      <defs>
        <radialGradient id="heartFill" cx="40%" cy="30%" r="75%">
          <stop offset="0%" stop-color="var(--heart-light)"/>
          <stop offset="55%" stop-color="var(--heart-mid)"/>
          <stop offset="100%" stop-color="var(--heart-dark)"/>
        </radialGradient>
      </defs>
      <path d="M184 60 C160 10 110 0 75 2 C30 5 0 45 0 100 C0 200 100 290 184 354 C268 290 369 200 369 100 C369 45 339 5 294 2 C259 0 208 10 184 60 Z" fill="url(#heartFill)"/>
    </svg>

    <div class="author-rule"></div>
    <p class="authors">Marla <span class="amp">&amp;</span> Walter Dunmore, PhD.</p>
  </main>
</body>
</html>
```